Business Card Design

Verdessa is a floral design company for weddings and special events.
Colours wanted are dark grey, aqua blue, white and black.
dark grey for the background, and the Verdessa in the aqua blue, rest of the writing in white and black etc.

Our floral design style is Rustic, textural, natural,
Wanting some kind of simplistic flower symbol next to the Verdessa see pictures.

Hi im so sorry I've changed some criteria. been confused on how this site works and what i want!! hope this is more straight forward. I also need clip art of the simple floral design i attached for my web site and also car magnets. thank you thank you thank YOU!!!! cherrs Bree

I have attached x5 ideas on where to place the lotus flower next to and around the verdessa. please use simliar colours of the flower as pictured. please cut out the white back ground from the flower. use only petals. use only lotus or the other icon provided per idea. still deciding on which one to use so waiting to see what looks best with your designs. thank you so very much in advance.!! Kindest REgards Bree

hi i am currently getting a logo design made through this also so can we wait until it is complete before any revisions are made. sorry about the delay!! thank you thank you thank you!! kind regards Bree

Reason: im having a logo made also to use on the cards. please hold off on any designs until this is received. thank you and so sorry about this!! cheers bR

Target Market(s)

modern elegant professional

Industry/Entity Type

Floral

Contact Information for Business Card

Front:
verdessa floral design (all lower case) floral design in smaller writting)
www.verdessafloraldesign.example.au

Back:
Wedding and event design

Bridget - 0498265140
verdessa@mailcove.example.au
Pauline-0455839061
floristpaulinecrowe@postly.example.com

Noosa-Tewantin, Sunshine coast, Qld

Font styles to use
Other font styles liked:
• corben, cookie

Colors
87d0c7
34b8a4
eaf2ce
ffffff
e4daeb
cfdeed

Requirements
Must have
• ; dark grey for back ground. or possible all white?
;verdessa floral designs in lower case and in blue' green aqua colour. all other writing in white.
icon which i can also use on the website. see pictures(i want to use the same on my web site.. if you can please make me an clip art icon also?
Nice to have
• simple elegant, earthy, flower icon
or second option icon of lotus looking flower verdessa inside
fonts please: verdessa floral design in (corben)
all writing on the back in (cookie)
maybe have the same icon clip art provided faintly on the back, bold on the front?
i also need car magnets to

```html
<!DOCTYPE html>
<html lang="en">
<head>
<meta charset="utf-8">
<title>verdessa floral design – Business Card</title>
<link rel="stylesheet" href="https://fonts.googleapis.com/css2?family=Corben&family=Marcellus&family=Montserrat:wght@500&display=swap">
<style>
  :root {
    --backdrop: #e6e6e4;
    --card-dark: #232324;
    --aqua: #1d8b95;
    --aqua-text: #2a9aa3;
    --silver: #a7a9ac;
    --white: #ffffff;
  }
  * { margin: 0; padding: 0; box-sizing: border-box; }
  html, body {
    width: 1200px; height: 901px; overflow: hidden;
    background: var(--backdrop);
  }
  .sheet {
    position: relative; width: 1200px; height: 901px;
    display: flex; align-items: center; justify-content: center; gap: 60px;
  }
  .card {
    position: relative; width: 520px; height: 297px;
    border-radius: 26px; overflow: hidden;
    background: var(--card-dark);
    box-shadow: 0 6px 18px rgba(0,0,0,.25);
  }
  .card__shapes { position: absolute; inset: 0; }
  .brand { position: absolute; color: var(--aqua-text); text-align: center; }
  .brand__mark {
    display: block; border: 5px solid var(--aqua); border-radius: 50%;
  }
  .brand__name {
    font-family: "Corben", serif; letter-spacing: .06em; line-height: 1;
  }
  .brand__tag {
    font-family: "Marcellus", serif; letter-spacing: .08em; line-height: 1;
  }

  /* contact card */
  .card--contact .brand__mark { position: absolute; left: 58px; top: 22px; width: 80px; height: 80px; }
  .card--contact .brand__text { position: absolute; left: 156px; top: 42px; text-align: left; }
  .card--contact .brand__name { font-size: 34px; }
  .card--contact .brand__tag { font-size: 18px; margin-top: 6px; }

  .contact {
    position: absolute; color: var(--white);
    font-family: "Montserrat", sans-serif; font-weight: 500;
    letter-spacing: .03em; font-size: 10.5px; line-height: 1.6;
  }
  .contact--place { left: 22px; top: 206px; width: 176px; text-align: center; }
  .contact__tagline { font-size: 12px; margin-bottom: 2px; }
  .contact--lines { left: 212px; top: 184px; }
  .contact__line { display: flex; align-items: center; gap: 7px; white-space: nowrap; }
  .contact__icon {
    width: 10px; height: 10px; border-radius: 50%; background: var(--white);
    flex: none;
  }

  /* logo card */
  .card--logo .brand { left: 0; right: 0; top: 40px; }
  .card--logo .brand__mark { width: 112px; height: 112px; margin: 0 auto 22px; }
  .card--logo .brand__name { font-size: 44px; }
  .card--logo .brand__tag { font-size: 22px; margin-top: 10px; }
</style>
</head>
<body>
<main class="sheet">

  <section class="card card--contact">
    <svg class="card__shapes" viewBox="0 0 520 297" preserveAspectRatio="none" aria-hidden="true">
      <path d="M0 148 C120 130 200 178 320 164 C420 152 480 130 520 126 L520 297 L0 297 Z" fill="var(--silver)"/>
      <path d="M0 160 C120 142 200 190 320 176 C420 164 480 142 520 138 L520 297 L0 297 Z" fill="var(--aqua)"/>
    </svg>
    <div class="brand">
      <span class="brand__mark"></span>
      <div class="brand__text">
        <div class="brand__name">verdessa</div>
        <div class="brand__tag">floral design</div>
      </div>
    </div>
    <div class="contact contact--place">
      <div class="contact__tagline">Wedding and event design</div>
      <div>Noosa-Tewantin,</div>
      <div>Sunshine Coast, Qld</div>
    </div>
    <div class="contact contact--lines">
      <div class="contact__line"><span class="contact__icon"></span>Bridget - 0498265140</div>
      <div class="contact__line"><span class="contact__icon"></span>verdessa@mailcove.example.au</div>
      <div class="contact__line"><span class="contact__icon"></span>Pauline - 0455839061</div>
      <div class="contact__line"><span class="contact__icon"></span>floristpaulinecrowe@postly.example.com</div>
      <div class="contact__line"><span class="contact__icon"></span>www.verdessafloraldesign.example.au</div>
    </div>
  </section>

  <section class="card card--logo">
    <div class="brand">
      <span class="brand__mark"></span>
      <div class="brand__name">verdessa</div>
      <div class="brand__tag">floral design</div>
    </div>
  </section>

</main>
</body>
</html>
```